Toravelle Works Luxury Candles

Luxury box design,, simple and sophisticated look,,

My collection of candles come in 5 different fragrances, i would like to be able to change the fragrance name on the boxes,,,,

I would like the outline of australia on the front down the bottom , (only small) to represent this is an australian product.

My boxes are white gloss,,,

Happy for you to use my current logo ,,, however you'll have to change Toravelle Nails to Toravelle Works.

```html
<!DOCTYPE html>
<html lang="en">
<head>
<meta charset="utf-8">
<title>Toravelle Works – Vanilla Caramel Candle Box</title>
<link rel="stylesheet" href="https://fonts.googleapis.com/css2?family=Poiret+One&display=swap">
<style>
  :root {
    --page-bg: #f4f4f2;
    --box-white: #ffffff;
    --box-edge: #e4e4e0;
    --gold-light: #f3d98a;
    --gold-mid: #d4a83c;
    --gold-deep: #a87a1e;
    --gold-text: #c08a3e;
    --name-ink: #1d1a14;
  }
  * { margin: 0; padding: 0; box-sizing: border-box; }
  html, body {
    width: 1200px;
    height: 811px;
    overflow: hidden;
    background: var(--page-bg);
  }
  .canvas {
    position: relative;
    width: 1200px;
    height: 811px;
    display: flex;
    align-items: center;
    justify-content: center;
  }
  .box-front {
    position: relative;
    width: 440px;
    height: 640px;
    background: var(--box-white);
    border: 1px solid var(--box-edge);
    box-shadow: 0 2px 10px rgba(0, 0, 0, 0.06);
  }
  .brand-band {
    position: absolute;
    left: 0;
    top: 175px;
    width: 100%;
    height: 120px;
    background: linear-gradient(90deg, var(--gold-light), var(--gold-mid) 35%, var(--gold-light) 55%, var(--gold-mid) 80%, var(--gold-light));
    display: flex;
    align-items: center;
    justify-content: center;
  }
  .brand-name {
    font-family: "Poiret One", sans-serif;
    font-size: 36px;
    font-weight: 400;
    letter-spacing: 1px;
    color: var(--name-ink);
  }
  .fragrance-name {
    position: absolute;
    left: 0;
    top: 380px;
    width: 100%;
    text-align: center;
    font-family: "Poiret One", sans-serif;
    font-size: 17px;
    letter-spacing: 3px;
    color: var(--gold-text);
  }
  .origin-map {
    position: absolute;
    left: 145px;
    top: 440px;
    width: 150px;
    height: 140px;
    border-radius: 10px;
    background: radial-gradient(ellipse at center, rgba(212, 168, 60, 0.22), rgba(243, 217, 138, 0.08) 75%);
  }
</style>
</head>
<body>
  <main class="canvas">
    <section class="box-front">
      <div class="brand-band" role="img" aria-label="Gold damask patterned band carrying the brand name">
        <span class="brand-name">Toravelle Works</span>
      </div>
      <p class="fragrance-name">Vanilla Caramel</p>
      <div class="origin-map" role="img" aria-label="Small gold outline map of Australia marking an Australian product"></div>
    </section>
  </main>
</body>
</html>
```